Holistic Psychologist needs contemporary business card

I am a psychologist working with adult clients face to face and online. The card needs to work for clients and also referring doctors and medical professionals. It needs to look warm, safe and trustable for clients, but clean and professional enough for doctors. Sometimes I also work in a corporate context.

I am holistic in my approach (mind-body-spirit) so anything conveying connection or integration or wholeness would be good. But again, clean and contemporary please. It can have a little bit of personality.
New logo uploaded.

Probably warm tones and plenty white space to write on one side.

My web pages:
http://mkcounsel.com.au
https://www.facebook.com/MarionKellerCounselling?ref=hl
Updates

Hi Designers .. I have decided I do need a new logo before finalising a design for the business cards.  I hope to have this available in 4 days from now.

Kindly,

Marion

New logo now posted, same brief.  Balance of masculine and feminine elements, plenty of white space on one side please.

Keen to see some card designs, thank-you.

Target Market(s)

Audience 1 - Males and females aged 25 years + seeking counselling or coaching. Audience 2 - doctors and health professionals who refer clients.

Industry/Entity Type

Medical

Contact Information for Business Card

Logo

Marion Keller
Registered Psychologist

M: 0491 582 034
www.mkcounsel.com.au
marion@mkcounsel.com.au
Little blue Facebook icon, with "marion keller counselling" printed near it.

Font styles to use
Sans Serif

Requirements
Nice to have
• You might want to play with the words "essential you"
Should not have
• Nothing cutesy or too literal

```html
<!DOCTYPE html>
<html lang="en">
<head>
<meta charset="utf-8">
<title>Marion Keller – Business Card Concepts</title>
<link rel="stylesheet" href="https://fonts.googleapis.com/css2?family=PT+Serif:wght@400;700&family=Questrial&family=Arimo&display=swap">
<style>
  :root {
    --paper: #ffffff;
    --frame-outer: #111111;
    --frame-red: #e21f26;
    --frame-trim: #8a8a8a;
    --brand-red: #e21f26;
    --brand-black: #000000;
    --brand-grey: #636466;
    --ink-light: #ffffff;
    --social-blue: #3b5998;
  }
  * { margin: 0; padding: 0; box-sizing: border-box; }
  html, body { width: 1200px; height: 768px; overflow: hidden; background: var(--paper); }
  .sheet { position: relative; width: 1200px; height: 768px; }

  .card { position: absolute; width: 556px; height: 343px; border: 2px solid var(--frame-outer); background: var(--paper); }
  .card::before { content: ""; position: absolute; left: 5px; top: 6px; right: 5px; bottom: 6px; border: 2px solid var(--frame-red); }
  .card::after { content: ""; position: absolute; left: 18px; top: 20px; right: 19px; bottom: 18px; border: 1px solid var(--frame-trim); }
  .card--front-red  { left: 31px;  top: 12px; }
  .card--back-red   { left: 610px; top: 12px; }
  .card--front-grey { left: 31px;  top: 414px; }
  .card--back-grey  { left: 610px; top: 414px; }

  .card > * { position: absolute; z-index: 1; }

  /* Front */
  .front__tab { left: 17px; top: 70px; width: 41px; height: 52px; background: var(--accent); }
  .front__bar { left: 327px; top: 70px; width: 206px; height: 52px; background: var(--bar); }
  .wordmark { font-family: "Questrial", sans-serif; font-weight: 400; color: var(--brand-red); white-space: nowrap; }
  .card > .front__wordmark { left: 80px; top: 77px; font-size: 28px; line-height: 38px; display: flex; align-items: center; gap: 10px; }
  .wordmark__dot { width: 22px; height: 22px; border-radius: 50%; background: var(--brand-red); }
  .front__web { right: 33px; top: 292px; font-family: "PT Serif", serif; font-size: 16px; color: var(--brand-red); }

  /* Back */
  .card > .back__name { left: 37px; top: 44px; font-family: "PT Serif", serif; font-weight: 400; font-size: 28px; line-height: 32px; color: var(--name); z-index: 3; }
  .back__band { left: 19px; top: 73px; width: 342px; height: 84px; background: var(--band); color: var(--ink-light); font-family: "PT Serif", serif; padding: 4px 0 0 18px; }
  .back__role { font-size: 16px; line-height: 22px; }
  .back__contact { font-size: 17px; line-height: 20px; margin-top: 12px; }
  .back__contact dt { float: left; font-weight: 700; margin-right: 6px; }
  .card > .back__mark { left: 372px; top: 82px; width: 112px; font-size: 24px; line-height: 28px; text-align: center; white-space: normal; }
  .back__bar { left: 493px; top: 73px; width: 42px; height: 84px; background: var(--bar); }
  .back__social { left: 37px; top: 289px; display: flex; align-items: center; gap: 6px; font-family: "Arimo", sans-serif; font-size: 15px; color: #111; }
  .social__square { width: 18px; height: 18px; background: var(--social-blue); }

  .scheme--red  { --accent: var(--brand-red);  --bar: var(--brand-black); --band: var(--brand-red);  --name: var(--brand-red); }
  .scheme--grey { --accent: var(--brand-grey); --bar: var(--brand-grey);  --band: var(--brand-grey); --name: var(--brand-grey); }
</style>
</head>
<body>
<main class="sheet">

  <section class="card card--front-red scheme--red">
    <div class="front__tab"></div>
    <div class="wordmark front__wordmark"><span class="wordmark__dot"></span>Marion Keller</div>
    <div class="front__bar"></div>
    <a class="front__web">www.mkcounsel.com.au</a>
  </section>

  <section class="card card--back-red scheme--red">
    <div class="back__band">
      <p class="back__role">Registered Psychologist</p>
      <dl class="back__contact">
        <dt>M:</dt><dd>0491 582 034</dd>
        <dt>E:</dt><dd>marion@mkcounsel.com.au</dd>
      </dl>
    </div>
    <h1 class="back__name">Marion Keller</h1>
    <div class="wordmark back__mark">Marion Keller</div>
    <div class="back__bar"></div>
    <p class="back__social"><span class="social__square"></span>marion keller counselling</p>
  </section>

  <section class="card card--front-grey scheme--grey">
    <div class="front__tab"></div>
    <div class="wordmark front__wordmark"><span class="wordmark__dot"></span>Marion Keller</div>
    <div class="front__bar"></div>
    <a class="front__web">www.mkcounsel.com.au</a>
  </section>

  <section class="card card--back-grey scheme--grey">
    <div class="back__band">
      <p class="back__role">Registered Psychologist</p>
      <dl class="back__contact">
        <dt>M:</dt><dd>0491 582 034</dd>
        <dt>E:</dt><dd>marion@mkcounsel.com.au</dd>
      </dl>
    </div>
    <h2 class="back__name">Marion Keller</h2>
    <div class="wordmark back__mark">Marion Keller</div>
    <div class="back__bar"></div>
    <p class="back__social"><span class="social__square"></span>marion keller counselling</p>
  </section>

</main>
</body>
</html>
```